Dane Morrow films- wedding and event films company website. DESKTOP AND MOBILE

We need a website for a high-end wedding and event film production company. Looking for a very modern and elegant design. my old website is www.danemorrowfilms.example

I like the "white/black/rose gold" color scheme of my logo.

really looking for a sleek modern design the breaths professional and artistic.

Target Market(s)

wedding and event films.

Industry/Entity Type

Film Production

Number of Pages Required

5+ page

Colors

Designer to choose colors to be used in the design.

Requirements
Must have
• website name will be www.danemorrowfilms.example
• tagline is "CINEMATIC STORIES ABOUT YOU"
• sections: HOME, CONTACT, ABOUT, FILMS, BLOG
• You can see my old website at danemorrowfilms.example
• Website about section:
• Dane Morrow Films was Established with the basis of truly cinematic and artistic films in mind. Dane and his team routinely travel the globe documenting weddings and events for high profile clients and discerning couples. Dane was born and raised in Maui Hawaii and has a unique approach to his films that embody the essence of a Hollywood film. Dane has spent the last 10 years traveling the world documenting corporate events and weddings with multiple Award winning production companies. In 2017 Dane decided to establish his own brand “Dane Morrow films” that will take everything he has learned with his past experiences and push it to the next level. Aside from his personal achievements, Dane is extremely passionate about his craft and always looks forward to handcrafting beautiful wedding/event films for his clients. The style of work is non-traditional and the day of filming is extremely unobtrusive (as we are looking for natural-candid/ raw emotions).
• If you are looking for the best price in town, we are probably not the best option, but if you’re looking for the best quality and peace of mind on your wedding day, then you’re in the right place. Dane Morrow Films is a boutique studio that only accepts a limited number of assignments per year. Inquire early to ensure availability.
• LINKS TO VIMEO VIDEOS THAT WILL BE IN THE "FILMS' SECTION.
• BRENT FILM TRAILER - https://clipvault.example/508114362
• BRENT FEATURE FILM - https://clipvault.example/617392048
• JUNE AND ROB'S WEDDING - https://clipvault.example/724958160
• DRONE DEMO REEL - https://clipvault.example/841576203
• WEDDING INDUSTRY EVENT PARTY - https://clipvault.example/962304817/a8d3e7b21c
• images that you can use on site are here: https://brigittolsenimages.proofbox.example/gallery/nora&felix/
• password is: meadow

```html
<!DOCTYPE html>
<html lang="en">
<head>
<meta charset="utf-8">
<title>Dane Morrow Films</title>
<link rel="stylesheet" href="https://fonts.googleapis.com/css2?family=Montserrat:wght@400;500;600;700&display=swap">
<style>
:root{
  --rose:#ad7451;
  --ink:#2f2f2f;
  --text:#555;
  --paper:#ffffff;
  --mist:#f3f3f3;
  --line:#d9d9d9;
}
*{box-sizing:border-box;margin:0;padding:0}
html,body{width:1200px;height:3285px;overflow:hidden}
body{position:relative;background:var(--mist);font-family:"Montserrat",sans-serif;color:var(--text)}
.abs{position:absolute}

/* header */
.site-header{left:0;top:0;width:1200px;height:131px;background:var(--paper)}
.brand{left:98px;top:66px;display:flex;align-items:center;gap:10px}
.brand-name{font-size:22px;font-weight:600;letter-spacing:1px;color:var(--ink);text-transform:uppercase}
.brand-mark{width:14px;height:14px;background:var(--rose)}
.contact-pill{top:26px;display:flex;align-items:center;gap:12px;font-size:12.5px;color:var(--ink);white-space:nowrap}
.icon-dot{width:38px;height:38px;border-radius:50%;background:var(--rose);display:flex;align-items:center;justify-content:center;flex:none}
.main-nav{top:88px;right:70px;display:flex}
.main-nav a{font-size:13px;font-weight:600;color:var(--ink);text-decoration:none;width:88px;text-align:center}

/* hero */
.hero{left:0;top:131px;width:1200px;height:614px;
  background:
    linear-gradient(100deg,rgba(90,100,110,.35) 0%,rgba(0,0,0,0) 30%),
    linear-gradient(180deg,#e6ddd0 0%,#d8c8b2 18%,#a9a196 34%,#8a8175 52%,#6e665c 72%,#5b544b 100%);
  clip-path:polygon(0 0,100% 0,100% 75%,50% 100%,0 75%)}
.hero-title{left:0;top:412px;width:1200px;text-align:center;font-size:38px;font-weight:700;color:#fff;letter-spacing:.5px;text-shadow:0 2px 6px rgba(0,0,0,.3)}

/* welcome */
.section-title{font-size:31px;font-weight:700;color:var(--ink);text-transform:uppercase}
.welcome-title{left:99px;top:785px}
.welcome-copy{left:99px;top:846px;width:585px;font-size:12.5px;line-height:25px;color:var(--text)}
.welcome-copy p+p{margin-top:12px}
.btn{display:inline-flex;align-items:center;justify-content:center;gap:8px;background:var(--rose);color:#fff;font-size:11.5px;font-weight:600;border-radius:20px;text-transform:uppercase;text-decoration:none}
.read-more{left:99px;top:1144px;width:142px;height:38px}
.portrait{left:720px;top:797px;width:378px;height:378px;border-radius:50%;border:4px solid #fff;box-shadow:0 0 0 2px var(--line);
  background:radial-gradient(circle at 50% 40%,#d8d8d8 0%,#a0a0a0 35%,#5a5a5a 65%,#2b2b2b 100%)}

/* couple */
.couple{left:0;top:1241px;width:1200px;height:690px;
  background:radial-gradient(ellipse at 52% 40%,#e4ddd3 0%,rgba(240,236,230,0) 40%),linear-gradient(180deg,#f7f5f2,#ece7e0 60%,#f2efea)}
.centre-title{left:0;width:1200px;text-align:center}
.couple-title{top:1280px;font-size:31px}
.subtitle{font-size:12px;color:var(--ink)}
.couple-sub{top:1325px}
.card-photo{top:1383px;height:300px;border:3px solid #fff;box-shadow:0 0 0 1px var(--line)}
.groom-photo{left:99px;width:434px;background:linear-gradient(115deg,#6f8a45 0%,#3b5a2a 35%,#e8ece6 52%,#26324a 62%,#1f2a3a 100%)}
.bride-photo{left:666px;width:432px;background:linear-gradient(180deg,#dfe3e8 0%,#b8c0c8 40%,#8d9196 62%,#5f5b55 100%)}
.bouquet{left:544px;top:1520px;width:110px;height:70px;border-radius:50%;background:#e8e2da}
.card-name{top:1712px;width:434px;text-align:center;font-size:22px;font-weight:500;color:var(--ink)}
.card-text{top:1752px;width:434px;text-align:center;font-size:12.5px;line-height:25px;color:var(--text)}
.view-more{top:1842px;width:128px;height:36px}
.slider-arrow{top:1525px}

/* videos */
.videos-title{top:1980px;font-size:31px}
.videos-sub{top:2027px}
.video{width:319px;height:210px;border:3px solid #fff;box-shadow:0 0 0 1px var(--line);overflow:hidden}
.player-bar{position:absolute;left:0;right:0;bottom:0;height:22px;background:rgba(20,25,30,.85);display:flex;align-items:center;padding:0 10px;gap:10px}
.player-bar .play{width:0;height:0;border-left:8px solid #fff;border-top:5px solid transparent;border-bottom:5px solid transparent}
.player-bar .track{flex:1;height:4px;background:#4aa3c8;border-radius:2px}
.player-bar .tools{width:50px;height:6px;background:#c9d2d8;border-radius:2px}

/* booking */
.booking{left:0;top:2590px;width:1200px;height:318px;background:linear-gradient(180deg,#9a9fa2,#7a8286 45%,#5c6466 75%,#4a4f50)}
.booking-title{top:2627px;font-size:29px;color:#fff}
.booking-sub{top:2672px;color:#fff}
.field-label{top:2745px;font-size:13px;font-weight:600;color:#fff;line-height:20px}
.field{top:2737px;width:213px;height:40px;background:#f2f2f2;border-radius:20px}
.select-caret{position:absolute;right:14px;top:16px;width:0;height:0;border-left:5px solid transparent;border-right:5px solid transparent;border-top:6px solid #777}
.send{left:546px;top:2822px;width:107px;height:32px;border:1px solid #fff;border-radius:16px;color:#fff;font-size:11px;font-weight:600;display:flex;align-items:center;justify-content:center}

/* footer */
.site-footer{left:0;top:2908px;width:1200px;height:377px;background:linear-gradient(180deg,#eeeeec,#f4f4f3 40%,#efeeec)}
.footer-brand{left:99px;top:3028px;display:flex;align-items:center;gap:10px}
.footer-blurb{left:99px;top:3092px;width:380px;font-size:12px;line-height:22px;color:var(--text)}
.footer-head{top:2950px;font-size:17px;font-weight:700;color:var(--ink);text-transform:uppercase}
.footer-links{left:534px;top:2988px;width:176px}
.footer-links li{list-style:none;height:54px;border-bottom:1px solid var(--line);display:flex;align-items:center;gap:14px;font-size:12px;color:var(--ink)}
.footer-links li:before{content:"›";color:var(--rose)}
.footer-contact{left:858px;top:2992px;font-size:12px;color:var(--ink)}
.footer-contact div{display:flex;align-items:center;gap:12px;height:50px}
.footer-rule{left:99px;top:3213px;width:1002px;height:1px;background:var(--line)}
.copyright{left:0;top:3236px;width:1200px;text-align:center;font-size:12px;color:var(--ink)}
</style>
</head>
<body>

<header class="site-header abs">
  <div class="brand abs"><span class="brand-mark"></span><span class="brand-name">Dane Morrow</span></div>
  <div class="contact-pill abs" style="left:626px">
    <span class="icon-dot"><svg width="16" height="12" viewBox="0 0 16 12"><rect x="0.5" y="0.5" width="15" height="11" fill="#fff"/><path d="M1 1l7 6 7-6" stroke="#ad7451" fill="none" stroke-width="1.4"/></svg></span>
    dane@danemorrowfilms.example
  </div>
  <div class="contact-pill abs" style="left:954px">
    <span class="icon-dot"><svg width="15" height="15" viewBox="0 0 24 24"><path fill="#fff" d="M6.6 10.8a15.1 15.1 0 006.6 6.6l2.2-2.2c.3-.3.7-.4 1-.2 1.1.4 2.3.6 3.6.6.6 0 1 .4 1 1V20c0 .6-.4 1-1 1A17 17 0 013 4c0-.6.4-1 1-1h3.5c.6 0 1 .4 1 1 0 1.3.2 2.5.6 3.6.1.3 0 .7-.2 1z"/></svg></span>
    (808) 555-0142
  </div>
  <nav class="main-nav abs"><a>Home</a><a>About</a><a>Films</a><a>Blog</a><a>Contact us</a></nav>
</header>

<section>
  <div class="hero abs" role="img" aria-label="Couple dancing on a rocky seaside path at sunset"></div>
  <h1 class="hero-title abs">"CINEMATIC STORIES ABOUT YOU"</h1>
</section>

<section>
  <h2 class="section-title welcome-title abs">Welcome to Dane Morrow Films</h2>
  <div class="welcome-copy abs">
    <p>At Dane Morrow Films we specialize in offering the finest in wedding and corporate cinematography. We offer a very modern and creative style for capturing your special moments with a beautiful and cinematic approach that enables up to produce the highest quality of films. Dane and his hand selected team have over 10 years of experience, and they strive to make the best films in the industry.</p>
    <p>We pride ourselves on remaining attentive to clients' needs, business practices rooted in integrity, and continually striving to be at the forefront of innovation in our industry.We pride ourselves on using the best quality cinema tools for our films. The equipment we use are industry standard cinematic tools used in hollywood movies. using such tools gives our films a truelly cinematic feel.</p>
  </div>
  <a class="btn read-more abs">Read more <svg width="12" height="8" viewBox="0 0 12 8"><path d="M0 4h10M7 1l3 3-3 3" stroke="#fff" fill="none" stroke-width="1.4"/></svg></a>
  <div class="portrait abs" role="img" aria-label="Black and white portrait of the filmmaker"></div>
</section>

<section>
  <div class="couple abs" role="img" aria-label="Faded photo of a bride and groom embracing"></div>
  <h2 class="section-title centre-title couple-title abs">Groom &amp; Bride</h2>
  <p class="subtitle centre-title couple-sub abs">About Bridal People</p>
  <svg class="slider-arrow abs" style="left:44px" width="20" height="32" viewBox="0 0 20 32"><path d="M16 2L4 16l12 14" stroke="#555" stroke-width="3" fill="none"/></svg>
  <svg class="slider-arrow abs" style="left:1134px" width="20" height="32" viewBox="0 0 20 32"><path d="M4 2l12 14L4 30" stroke="#555" stroke-width="3" fill="none"/></svg>
  <div class="card-photo groom-photo abs" role="img" aria-label="Groom in a navy suit beside white calla lilies"></div>
  <div class="bouquet abs" role="img" aria-label="Small bouquet illustration"></div>
  <div class="card-photo bride-photo abs" role="img" aria-label="Bride in a white gown on a coastal cliff"></div>
  <h3 class="card-name abs" style="left:99px">NORA</h3>
  <p class="card-text abs" style="left:99px">Lorem ipsum dolor sit amet, consectetur adipiscing elit. Quisque congue maximus tellus ut porta. Sed ultrices nibh nunc, sapien varius ut. Etiam sed tempor arcu, id dapibus diam. Donec at dolor leo.</p>
  <a class="btn view-more abs" style="left:252px">View more &gt;&gt;</a>
  <h3 class="card-name abs" style="left:665px">FELIX</h3>
  <p class="card-text abs" style="left:665px">Lorem ipsum dolor sit amet, consectetur adipiscing elit. Quisque congue maximus tellus ut porta. Sed ultrices nibh nunc, sapien varius ut. Etiam sed tempor arcu, id dapibus diam. Donec at dolor leo.</p>
  <a class="btn view-more abs" style="left:818px">View more &gt;&gt;</a>
</section>

<section>
  <h2 class="section-title centre-title videos-title abs">Watch Our Video</h2>
  <p class="subtitle centre-title videos-sub abs">Our Best Films</p>
  <div class="video abs" style="left:101px;top:2085px;background:linear-gradient(90deg,#5a2e3e 0%,#8a5a60 30%,#3a2a34 55%,#c8bfc4 80%,#6a5a66 100%)" role="img" aria-label="Film still of wedding guests laughing"><div class="player-bar"><span class="play"></span><span class="track"></span><span class="tools"></span></div></div>
  <div class="video abs" style="left:440px;top:2085px;background:linear-gradient(180deg,#9fb3c8 0%,#6f879c 35%,#3f5566 55%,#2c3d47 100%)" role="img" aria-label="Film still of a mountain lake"><div class="player-bar"><span class="play"></span><span class="track"></span><span class="tools"></span></div></div>
  <div class="video abs" style="left:777px;top:2085px;background:linear-gradient(90deg,#3f5a30 0%,#8a7a66 35%,#c04a3a 55%,#e8e2da 75%,#5a6a3a 100%)" role="img" aria-label="Film still of a garden wedding ceremony"><div class="player-bar"><span class="play"></span><span class="track"></span><span class="tools"></span></div></div>
  <div class="video abs" style="left:101px;top:2315px;background:linear-gradient(180deg,#e8c0a0 0%,#d19a78 35%,#8a5a48 60%,#5a3e34 100%)" role="img" aria-label="Film still of a couple on a beach at sunset"><div class="player-bar"><span class="play"></span><span class="track"></span><span class="tools"></span></div></div>
  <div class="video abs" style="left:440px;top:2315px;background:linear-gradient(90deg,#3f5a35 0%,#6b7a5a 30%,#e6e2da 45%,#1f2430 65%,#4a5a3a 100%)" role="img" aria-label="Film still of a couple under trees"><div class="player-bar"><span class="play"></span><span class="track"></span><span class="tools"></span></div></div>
  <div class="video abs" style="left:777px;top:2315px;background:linear-gradient(180deg,#e2e6ea 0%,#a8b8c6 35%,#2e4a6a 55%,#7a6a60 80%,#5a6470 100%)" role="img" aria-label="Film still of a crowd at an outdoor event"><div class="player-bar"><span class="play"></span><span class="track"></span><span class="tools"></span></div></div>
</section>

<section>
  <div class="booking abs" role="img" aria-label="Coastline with a lighthouse"></div>
  <h2 class="section-title centre-title booking-title abs">Are You Attending?</h2>
  <p class="subtitle centre-title booking-sub abs">Start Your Booking Here !</p>
  <span class="field-label abs" style="left:99px">Name</span>
  <div class="field abs" style="left:173px"></div>
  <span class="field-label abs" style="left:426px">No. Of Guests</span>
  <div class="field abs" style="left:537px"><span class="select-caret"></span></div>
  <span class="field-label abs" style="left:789px">Party You<br>Want</span>
  <div class="field abs" style="left:887px"><span class="select-caret"></span></div>
  <div class="send abs">SEND</div>
</section>

<footer class="site-footer abs" role="img" aria-label="Faint misty hillside behind the footer"></footer>
<div class="footer-brand abs"><span class="brand-mark"></span><span class="brand-name">Dane Morrow</span></div>
<p class="footer-blurb abs">Cras sagittis sodales nunc, sed suscipit erat imperdiet eu. Sed pretium metus sit amet velit congue, ac lobortis elit efficitur. Etiam sagittis erat eget mi</p>
<h4 class="footer-head abs" style="left:534px">Important Links</h4>
<ul class="footer-links abs"><li>About</li><li>Films</li><li>Blog</li></ul>
<h4 class="footer-head abs" style="left:858px">Contact Us</h4>
<div class="footer-contact abs">
  <div><svg width="12" height="12" viewBox="0 0 24 24"><path fill="#ad7451" d="M6.6 10.8a15.1 15.1 0 006.6 6.6l2.2-2.2c.3-.3.7-.4 1-.2 1.1.4 2.3.6 3.6.6.6 0 1 .4 1 1V20c0 .6-.4 1-1 1A17 17 0 013 4c0-.6.4-1 1-1h3.5c.6 0 1 .4 1 1 0 1.3.2 2.5.6 3.6.1.3 0 .7-.2 1z"/></svg>dane@danemorrowfilms.example</div>
  <div><svg width="13" height="10" viewBox="0 0 16 12"><rect width="16" height="12" fill="#ad7451"/><path d="M1 1l7 6 7-6" stroke="#fff" fill="none" stroke-width="1.4"/></svg>(808) 555-0142</div>
</div>
<div class="footer-rule abs"></div>
<p class="copyright abs">Copyright © 2017 &nbsp;Dane Morrow Films - All Rights Reserved</p>

</body>
</html>
```